Mirela Dawn Business Card Design

I need a business card for my daughter. She has it all described in the file below. But it needs to be square in shape. http://www.mireladawn.example is her web site

Target Market(s)

18-35 year old women

Industry/Entity Type

Fashion

Contact Information for Business Card

Please look at the attached file as it has all the details.

Requirements
Must have
• Please look at the attached file as it has all the details.
Nice to have
Should not have

```html
<!DOCTYPE html>
<html lang="en">
<head>
<meta charset="utf-8">
<title>Mirela Dawn – Square Business Card</title>
<link rel="stylesheet" href="https://fonts.googleapis.com/css2?family=Cinzel:wght@400&family=Questrial&display=swap">
<style>
  :root {
    --canvas-bg: #8f8f8f;
    --ink: #0c0c0c;
    --white: #ffffff;
    --blush: #fbd9e5;
    --blush-panel: rgba(236, 196, 210, 0.93);
    --slate-dark: #1b1b1b;
    --slate-mid: #2e2e2e;
  }
  * { box-sizing: border-box; margin: 0; padding: 0; }
  html, body { width: 1200px; height: 900px; overflow: hidden; }
  body { background: var(--canvas-bg); position: relative; font-family: "Questrial", sans-serif; }

  .card { position: absolute; top: 256px; width: 399px; height: 399px; }

  /* Front */
  .card-front { left: 228px; }
  .front-texture {
    position: absolute; inset: 0;
    background: radial-gradient(circle at 40% 35%, var(--slate-mid), var(--slate-dark) 75%);
  }
  .name-panel {
    position: absolute; left: 25px; top: 116px; width: 347px; height: 167px;
    background: var(--blush-panel); text-align: center;
  }
  .name {
    font-family: "Cinzel", serif; font-weight: 400; font-size: 44px;
    color: var(--ink); letter-spacing: 1px; margin-top: 28px; line-height: 1;
  }
  .name-rule { width: 217px; height: 4px; background: var(--white); margin: 24px auto 0; }
  .tagline { font-size: 18px; letter-spacing: 2px; color: var(--ink); margin-top: 20px; }

  /* Back */
  .card-back { left: 669px; background: var(--ink); padding: 12px; }
  .back-inner { position: relative; width: 100%; height: 100%; background: var(--blush); }
  .role-band {
    position: absolute; left: 9px; top: 12px; width: 356px; height: 51px;
    background: var(--ink); color: var(--white);
    font-size: 13.5px; display: flex; align-items: center; justify-content: center;
  }
  .contact-list { position: absolute; left: 41px; top: 92px; list-style: none; }
  .contact-item { display: flex; align-items: center; height: 39px; font-size: 18px; color: var(--ink); }
  .contact-mark { width: 30px; height: 30px; border-radius: 50%; background: var(--ink); margin-right: 9px; flex: none; }
  .contact-icon { width: 30px; height: 30px; margin-right: 9px; flex: none; }
  .site-links { position: absolute; left: 45px; top: 273px; }
  .site-line { font-size: 18px; color: var(--ink); height: 34px; line-height: 34px; }
  .site-label { font-family: "Cinzel", serif; font-size: 20px; }
</style>
</head>
<body>
  <section class="card card-front" aria-label="Card front">
    <div class="front-texture" role="img" aria-label="Dark scratched slate texture background"></div>
    <div class="name-panel">
      <h1 class="name">MIRELA DAWN</h1>
      <div class="name-rule"></div>
      <p class="tagline">FLUENT IN FASHION</p>
    </div>
  </section>

  <section class="card card-back" aria-label="Card back">
    <div class="back-inner">
      <div class="role-band">blogger &amp; vlogger // beauty-fashion-travel</div>
      <ul class="contact-list">
        <li class="contact-item"><span class="contact-mark"></span>snapfolio.example/mireladawnxo</li>
        <li class="contact-item"><span class="contact-mark"></span>chirpline.example/mireladawnxo</li>
        <li class="contact-item"><span class="contact-mark"></span>@mireladawnxo</li>
        <li class="contact-item">
          <svg class="contact-icon" viewBox="0 0 30 30" aria-hidden="true">
            <circle cx="15" cy="15" r="15" fill="#0c0c0c"/>
            <rect x="7.5" y="10" width="15" height="10" fill="#ffffff"/>
            <path d="M7.5 10 L15 16 L22.5 10" fill="none" stroke="#0c0c0c" stroke-width="1.4"/>
          </svg>mirela@mireladawn.example
        </li>
      </ul>
      <div class="site-links">
        <p class="site-line"><span class="site-label">BLOG:</span> mireladawn.example</p>
        <p class="site-line"><span class="site-label">VIDEOS:</span> vidstream.example/mireladawn</p>
      </div>
    </div>
  </section>
</body>
</html>
```